Looking for a creative label design for our retail coffee bags

We are a coffee manufacturer (coffee roaster) looking to re-brand our retail label for our coffee bags. Our main coffee blend that we sell is our Harborline Velvet Blend. You can use this name when creating the label. We are going for a look that represents our company as a coffee roaster. Please reference our website (www.brindlemugworks.com) and our Facebook page to learn more about our company and to give you more inspiration on creating this design.

Target Market(s)

Retail customers/grocery stores

Industry/Entity Type

Manufacturer

Requirements
Must have
• The size of the label has to be 3" width x 4" height

Logo must be Black
Nice to have
• We currently incorporate a color on our labels for each blend. For example, Harborline Velvet Blend (royal blue), Decaffeinated Blend (red), Breakfast Blend (green), Flavored coffees (gold).

Rustic/vintage style

```html
<!DOCTYPE html>
<html lang="en">
<head>
<meta charset="utf-8">
<title>Brindle Mugworks – Harborline Velvet Blend Label</title>
<link rel="stylesheet" href="https://fonts.googleapis.com/css2?family=Josefin+Sans:wght@300;400;600&family=League+Spartan:wght@700&display=swap">
<style>
  :root {
    --ink: #1c1c1c;
    --gold: #d29c32;
    --gold-soft: #a8792a;
    --paper: #ffffff;
  }
  * { margin: 0; padding: 0; box-sizing: border-box; }
  html, body { width: 900px; height: 1200px; overflow: hidden; background: var(--ink); }
  .label {
    position: relative;
    width: 900px;
    height: 1200px;
    overflow: hidden;
    font-family: "Josefin Sans", sans-serif;
    color: var(--paper);
  }
  .bean-field {
    position: absolute;
    inset: 0;
    background:
      radial-gradient(ellipse at 50% 50%, var(--ink) 45%, rgba(28,28,28,0) 85%),
      linear-gradient(135deg, var(--gold-soft), var(--gold) 50%, var(--gold-soft));
  }
  .info-shade {
    position: absolute;
    left: 57px; top: 265px;
    width: 800px; height: 880px;
    background: var(--ink);
  }
  .info-panel {
    position: absolute;
    left: 93px; top: 290px;
    width: 726px; height: 823px;
    border: 4px solid var(--paper);
    background: var(--ink);
  }
  .seal { position: absolute; left: 0; top: 0; width: 900px; height: 1200px; }
  .seal-tagline {
    font-family: "Josefin Sans", sans-serif;
    font-size: 12px;
    font-weight: 400;
    letter-spacing: 2px;
    fill: var(--paper);
  }
  .brand-name {
    position: absolute;
    left: 290px; top: 168px;
    width: 340px;
    text-align: center;
    font-family: "Josefin Sans", sans-serif;
    font-weight: 300;
    font-size: 50px;
    line-height: 1;
    letter-spacing: 2px;
    color: var(--paper);
  }
  .brand-name span { display: block; margin-top: 8px; }
  .blend-title {
    position: absolute;
    left: 186px; top: 522px;
    width: 536px;
    text-align: center;
    font-family: "League Spartan", sans-serif;
    font-weight: 700;
    font-size: 45px;
    line-height: 1;
    color: var(--paper);
  }
  .blend-title .rule {
    display: block;
    height: 6px;
    background: var(--gold);
    margin: 12px 0 14px;
  }
  .specs {
    position: absolute;
    left: 122px; top: 690px;
    width: 671px;
    list-style: none;
  }
  .spec {
    display: flex;
    justify-content: space-between;
    align-items: flex-end;
    height: 87.5px;
    padding-bottom: 12px;
    border-bottom: 3px solid var(--paper);
    font-size: 40px;
    font-weight: 300;
    line-height: 1;
  }
  .spec:first-child { height: 60px; }
  .spec:last-child { border-bottom: none; }
  .roast-scale {
    display: flex;
    align-items: center;
    flex: 1;
    margin-left: 52px;
    justify-content: space-between;
    font-size: 30px;
  }
  .roast-dark { display: flex; align-items: center; gap: 12px; }
  .roast-dot {
    width: 24px; height: 24px;
    border-radius: 50%;
    background: var(--paper);
  }
</style>
</head>
<body>
<div class="label">
  <div class="bean-field" role="img" aria-label="Repeating pattern of gold coffee beans on a black background"></div>
  <div class="info-shade"></div>
  <div class="info-panel"></div>

  <svg class="seal" viewBox="0 0 900 1200" aria-hidden="true">
    <defs>
      <path id="tagline-arc" d="M 245 325 A 226 226 0 0 0 675 325"/>
    </defs>
    <circle cx="460" cy="255" r="214" fill="var(--ink)"/>
    <circle cx="460" cy="255" r="195" fill="var(--ink)" stroke="var(--paper)" stroke-width="7"/>
    <text class="seal-tagline">
      <textPath href="#tagline-arc" startOffset="50%" text-anchor="middle">PROUDLY ROASTED IN ASHFORD FALLS, OH SINCE 1994.</textPath>
    </text>
  </svg>

  <div class="brand-name">BRINDLE<span>MUGWORKS</span></div>

  <h1 class="blend-title">HARBORLINE<span class="rule"></span>VELVET BLEND</h1>

  <ul class="specs">
    <li class="spec"><span>Altitude:</span><span>1800–1900</span></li>
    <li class="spec"><span>Processing:</span><span>Washed</span></li>
    <li class="spec"><span>Flavors:</span><span>Rich aroma</span></li>
    <li class="spec"><span>Roast:</span>
      <span class="roast-scale">
        <span>Light</span>
        <span>Medium</span>
        <span class="roast-dark">Dark <span class="roast-dot"></span></span>
      </span>
    </li>
    <li class="spec"><span>Weight:</span><span>500g</span></li>
  </ul>
</div>
</body>
</html>
```